Boldheart Youth Academy Website Design- Superhero Theme

Redesign website- Superhero theme. The current site is https://www.boldheartyouthacademy.example/. I would like a superhero theme like the wallpaper picture attached. I would also like to incorporate the GCA WPA 17 goals. The theme is Boldheart Youth Academy: Training the Next Generation of Kid- Superheroes
The site will offer different courses. Here is a link to my current course offerings: https://learnloft.example/teachers/boldheart-youth-academy#qwTmRbZk81
Classes I would like to feature courses like: Tiny Trailblazers, Confident Talks and Campaigns: How to Lift Your Message for Change and etc. I need a website that is bright, vibrant, and superhero fun.
Company Information:
"The reasonable man adapts himself to the world; the unreasonable one persists in trying to adapt the world to himself. Therefore all progress depends on the unreasonable man/ woman [& Kid]."
- Harold Quentin Mayfield
KIDS CAN BE BOLDHEARTED TOO!
Boldheart Youth Academy is a social, educational enterprise, training the next generation of kid superheroes. The goal is to train kids to become unreasonable thinkers to see opportunity where adults see problems. The objective is to create opportunities for kids to tackle the goals set by the Global Civic Alliance 17 World Progress Aims. Topics addressed, such as poverty, environmental, and other issues of his or her interest.
Boldheart Youth Academy creates a safe, peer to peer, coach-led environment to facilitate and inspire world changers, as they learn how to release their fight for good. The fall and spring semester classes, one-day workshops, and summer camps are filled with brain-based learning activities and a creative design curriculum to help kids develop his or her social entrepreneurial super-powers.
Updates
Need extra time - due to holiday.
Target Market(s)
Parents looking for virtual classes for their kids.
Industry/Entity Type
Technical Training School
Coding
Coded - Design and coding required
Number of Pages Required
5+ page
Font styles to use
Requirements
Must have
- Superhero theme and GCA WPA goals incorporated! Ability to add my registration link to it using PELTON tools.
Nice to have
- Colors that are bright and match the superhero wallpaper I attached to files.
Should not have
- Cheap wordpress must look very high level - like an elite college but for kids.

```html
<!DOCTYPE html>
<html lang="en">
<head>
<meta charset="utf-8">
<title>Boldheart Youth Academy — Home</title>
<link rel="stylesheet" href="https://fonts.googleapis.com/css2?family=Bangers&family=Didact+Gothic&family=Barlow+Condensed:wght@600&display=swap">
<style>
  :root {
    --sky: #5fc8ec;
    --sky-light: #86dbf6;
    --sky-deep: #3eb2de;
    --band-green: #8cc63f;
    --ink: #111111;
    --white: #ffffff;
    --cloud-edge: #2b2b2b;
    --yellow: #f8c400;
    --red: #e4202a;
    --blue: #2ea7e0;
    --pink: #ec1e79;
    --register-green: #2f9d3a;
    --orange: #e07a1c;
    --frame-hole: #6fd0f2;
  }
  * { box-sizing: border-box; margin: 0; padding: 0; }
  html, body { width: 1200px; height: 1149px; overflow: hidden; }
  body {
    position: relative;
    background: radial-gradient(circle at 50% 40%, var(--sky-light) 0%, var(--sky) 45%, var(--sky-deep) 100%);
    font-family: "Didact Gothic", sans-serif;
  }
  .top-band {
    position: absolute; left: 0; top: 0; width: 1200px; height: 106px;
    background: var(--band-green);
  }
  .brand-badge {
    position: absolute; left: -40px; top: -70px; width: 330px; height: 250px;
    background: var(--white); border: 5px solid var(--ink); border-radius: 50%;
  }
  .brand {
    position: absolute; left: 20px; top: 62px; width: 250px; text-align: center;
  }
  .brand-mark {
    display: inline-block; width: 26px; height: 26px; border-radius: 50%;
    background: var(--orange); margin-bottom: 6px;
  }
  .brand-name {
    font-family: "Didact Gothic", sans-serif; font-size: 17px; color: var(--ink); line-height: 1.1;
  }
  .brand-tagline {
    font-family: "Barlow Condensed", sans-serif; font-weight: 600; font-size: 9px;
    color: var(--orange); margin-top: 3px;
  }
  .main-nav { position: absolute; top: 20px; left: 0; width: 1200px; height: 66px; }
  .nav-item {
    position: absolute; width: 94px; height: 62px; border-radius: 46% 54% 48% 52% / 55% 50% 50% 45%;
    display: flex; align-items: center; justify-content: center; text-align: center;
    font-family: "Bangers", sans-serif; color: var(--white); text-decoration: none;
    -webkit-text-stroke: 1px var(--ink); paint-order: stroke fill;
    letter-spacing: 0.5px; line-height: 0.95;
  }
  .nav-home { left: 544px; background: var(--yellow); font-size: 26px; }
  .nav-online { left: 674px; background: var(--red); font-size: 17px; }
  .nav-afterschool { left: 804px; background: var(--blue); font-size: 7px; -webkit-text-stroke: 0.4px var(--ink); }
  .nav-about { left: 934px; background: var(--pink); font-size: 24px; }
  .nav-register { left: 1066px; background: var(--white); border: 2px solid var(--ink); color: var(--register-green); font-size: 20px; }
  .intro-reel {
    position: absolute; left: 448px; top: 151px; width: 304px; height: 234px; background: var(--white);
  }
  .reel-holes { position: absolute; left: 13px; width: 280px; display: flex; justify-content: space-between; }
  .reel-holes.top { top: 10px; }
  .reel-holes.bottom { top: 207px; }
  .reel-holes span { width: 16px; height: 18px; border-radius: 3px; background: var(--frame-hole); }
  .reel-screen {
    position: absolute; left: 7px; top: 36px; width: 290px; height: 162px; border-radius: 8px;
    background: radial-gradient(circle at 50% 50%, #2a8fd0 0 14%, #eb8a2a 15%, var(--orange) 100%);
  }
  .welcome {
    position: absolute; left: 0; top: 405px; width: 1200px; text-align: center;
    font-family: "Bangers", sans-serif; font-size: 38px; line-height: 44px; color: var(--white);
    -webkit-text-stroke: 2px var(--ink); paint-order: stroke fill;
    text-shadow: 3px 3px 0 var(--ink); letter-spacing: 1px;
  }
  .cloud-art { position: absolute; left: 0; top: 0; }
  .founder-quote {
    position: absolute; left: 436px; top: 690px; width: 340px;
    font-size: 13px; line-height: 18.2px; color: var(--ink); letter-spacing: 0.3px;
  }
  .founder-quote cite { font-style: italic; display: block; }
</style>
</head>
<body>
  <header>
    <div class="top-band"></div>
    <div class="brand-badge"></div>
    <div class="brand">
      <span class="brand-mark"></span>
      <div class="brand-name">Boldheart Youth Academy</div>
      <div class="brand-tagline">Training the Next Generation of Kid-Superheroes</div>
    </div>
    <nav class="main-nav">
      <a class="nav-item nav-home" href="#">Home</a>
      <a class="nav-item nav-online" href="#">Online<br>Classes</a>
      <a class="nav-item nav-afterschool" href="#">After-School Programs<br>and<br>Workshop</a>
      <a class="nav-item nav-about" href="#">About</a>
      <a class="nav-item nav-register" href="#">Register</a>
    </nav>
  </header>

  <main>
    <div class="intro-reel">
      <div class="reel-holes top"><span></span><span></span><span></span><span></span><span></span><span></span><span></span><span></span></div>
      <div class="reel-screen" role="img" aria-label="Animated intro video: the Earth at the centre surrounded by orbiting shapes on an orange field"></div>
      <div class="reel-holes bottom"><span></span><span></span><span></span><span></span><span></span><span></span><span></span><span></span></div>
    </div>

    <h1 class="welcome">Welcome to<br>Boldheart Youth Academy</h1>

    <svg class="cloud-art" width="1200" height="1149" viewBox="0 0 1200 1149" aria-hidden="true">
      <g fill="var(--cloud-edge)">
        <circle cx="415" cy="585" r="45"/><circle cx="450" cy="580" r="40"/><circle cx="430" cy="610" r="35"/>
        <circle cx="720" cy="590" r="45"/><circle cx="755" cy="600" r="40"/><circle cx="735" cy="622" r="35"/>
        <circle cx="560" cy="660" r="100"/><circle cx="680" cy="655" r="95"/><circle cx="470" cy="740" r="90"/>
        <circle cx="735" cy="735" r="95"/><circle cx="600" cy="760" r="135"/><circle cx="510" cy="835" r="75"/>
        <circle cx="660" cy="825" r="90"/><circle cx="730" cy="795" r="65"/>
        <circle cx="455" cy="865" r="55"/><circle cx="495" cy="860" r="45"/><circle cx="470" cy="895" r="45"/>
        <circle cx="642" cy="925" r="30"/><circle cx="668" cy="920" r="25"/>
      </g>
      <g fill="var(--white)">
        <circle cx="415" cy="585" r="38"/><circle cx="450" cy="580" r="33"/><circle cx="430" cy="610" r="28"/>
        <circle cx="720" cy="590" r="38"/><circle cx="755" cy="600" r="33"/><circle cx="735" cy="622" r="28"/>
        <circle cx="560" cy="660" r="93"/><circle cx="680" cy="655" r="88"/><circle cx="470" cy="740" r="83"/>
        <circle cx="735" cy="735" r="88"/><circle cx="600" cy="760" r="128"/><circle cx="510" cy="835" r="68"/>
        <circle cx="660" cy="825" r="83"/><circle cx="730" cy="795" r="58"/>
        <circle cx="455" cy="865" r="48"/><circle cx="495" cy="860" r="38"/><circle cx="470" cy="895" r="38"/>
        <circle cx="642" cy="925" r="23"/><circle cx="668" cy="920" r="18"/>
      </g>
    </svg>

    <blockquote class="founder-quote">
      <p>The reasonable man adapts himself to the world; the unreasonable one persists in trying to adapt the world to himself. Therefore all progress depends on the unreasonable man/ woman [&amp; Kid].</p>
      <cite>- Harold Quentin Mayfield</cite>
    </blockquote>
  </main>
</body>
</html>
```